Professional & Modern Technology Business Card

We need a business card for our software/technology firm. Our services include Program/Project Management, Project Controls and Enterprise Analytics. Our clients are usually in the Aviation, Public Works, Transportation and Electric & Water Utility industries. We serve both public and private clients. Would like a very professional, conservative but somewhat modern design. Design, Develop, Deploy is the corporate tagline. We have two offices. The headquarters is in Atlanta, GA and a satellite office In Savannah, GA. Corporate Logo Attached.
Looking to do website and corporate brochure after the successful completion of this project. Would like to begin a working relationship with best designers.
Tagline: Design, Develop, Deploy
Website: www.quelvanesystems.example
My Name: Marla Dunstead
My Title: CEO
Email: mdunstead@quelvanesystems.example
Atlanta Address:
87 Corliss Avenue, #2291
Atlanta, GA 30301
Office: 404.555.0182
Fax: 404.555.0147
Mobile: 404.555.0163
Savannah Address:
350 West Harrow Bend Road
Suite 720
Savannah, GA 31401
Office: 912.555.0139
Fax: 404.555.0147
Mobile: 404.555.0163
Updates
Please include the email address in your designs: mdunstead@quelvanesystems.example.
I appreciate everyone's design efforts. Just a few notes:
1. Please remove the mobile number from the cards
2. The backs of the cards can be utilized for writing notes. Make sure your design on the back of the card is conducive to clearly adding writing if needed.
3. No black backgrounds please
4. Only use the corporate logo on the front of the card. You can use portions of the logo design, but not the logo in totality.
Thank You
Industry/Entity Type
Conservative
Look and feel
Each slider illustrates characteristics of the customer's brand and the style your logo design should communicate.

```html
<!DOCTYPE html>
<html lang="en">
<head>
<meta charset="utf-8">
<title>Quelvane Systems, Inc. — Business Card</title>
<link rel="stylesheet" href="https://fonts.googleapis.com/css2?family=Arimo:wght@400;700&display=swap">
<style>
  :root {
    --stage: #ecebe8;
    --card: #ffffff;
    --ink: #111111;
    --name-green: #7ed321;
    --label-cyan: #2bb8ea;
    --label-green: #8fd14f;
    --mark-gold: #d8b72a;
    --shadow: rgba(0, 0, 0, 0.18);
  }
  * { box-sizing: border-box; margin: 0; padding: 0; }
  html, body {
    width: 1200px; height: 800px; overflow: hidden;
    background: var(--stage);
    font-family: "Arimo", Arial, sans-serif;
    color: var(--ink);
  }
  .stage { position: relative; width: 1200px; height: 800px; }
  .card {
    position: absolute; top: 245px;
    width: 525px; height: 300px;
    background: var(--card);
    box-shadow: 0 6px 18px var(--shadow);
  }
  .card--front { left: 55px; }
  .card--back { left: 620px; }

  /* Front */
  .brand {
    position: absolute; left: 0; right: 0; top: 92px;
    display: flex; align-items: center; justify-content: center; gap: 18px;
  }
  .brand__dot {
    width: 46px; height: 46px; border-radius: 50%;
    background: var(--mark-gold);
  }
  .brand__name {
    font-weight: 700; font-size: 40px; line-height: 1.05;
    color: var(--ink); letter-spacing: -0.5px;
  }
  .tagline {
    position: absolute; left: 0; right: 0; bottom: 46px;
    text-align: center; font-weight: 700; font-size: 19px;
  }

  /* Back */
  .holder {
    position: absolute; left: 180px; top: 30px; text-align: center;
    font-weight: 700;
  }
  .holder__name { color: var(--name-green); font-size: 20px; }
  .holder__title { font-size: 17px; margin-top: 4px; }
  .office {
    position: absolute; font-weight: 700; font-size: 10.5px; line-height: 1.55;
  }
  .office__label { color: var(--label-cyan); }
  .office--atlanta { left: 400px; top: 110px; }
  .office--savannah { left: 22px; top: 160px; }
  .contact {
    position: absolute; left: 205px; top: 245px;
    font-weight: 700; font-size: 10.5px; line-height: 1.55;
    display: grid; grid-template-columns: 46px auto;
  }
  .contact__label { color: var(--label-green); }
</style>
</head>
<body>
<main class="stage">
  <section class="card card--front" aria-label="Card front">
    <div class="brand">
      <span class="brand__dot"></span>
      <span class="brand__name">Quelvane<br>Systems, Inc.</span>
    </div>
    <p class="tagline">Design, Develop, Deploy</p>
  </section>

  <section class="card card--back" aria-label="Card back">
    <div class="holder">
      <p class="holder__name">Marla Dunstead</p>
      <p class="holder__title">CEO</p>
    </div>

    <address class="office office--atlanta">
      <span class="office__label">Atlanta Address:</span><br>
      87 Corliss Avenue, #2291<br>
      Atlanta, GA 30301<br>
      Office: 404.555.0182<br>
      Fax: 404.555.0147
    </address>

    <address class="office office--savannah">
      <span class="office__label">Savannah Address:</span><br>
      350 West Harrow Bend Road<br>
      Suite 720<br>
      Savannah, GA 31401<br>
      Office: 912.555.0139<br>
      Fax: 404.555.0147
    </address>

    <div class="contact">
      <span class="contact__label">Email:</span><span>mdunstead@quelvanesystems.example</span>
      <span class="contact__label">Web:</span><span>www.quelvanesystems.example</span>
    </div>
  </section>
</main>
</body>
</html>
```